Marlow Realty Real Estate Brokerage Recruiting Flyer

We are a real estate brokerage looking to hire more real estate agents. We need to list everything we have to offer as a company so real estate agents will join our company. this is our company website: www.Marlowrealty.example .

100% COMMISSION NO MONTHLY FEE
$450 Flat Transaction FEE

What We Offer:
24/7 Office Access
Free E & O Insurance for 1st Year
Free Online CE and PLE
Free 1,000 Business Cards
Free Professional Social Media Marketing
Free Printing, Scanning, and Copies
Free Buyer and Seller Presentation Packages
Free Filquay Cloud Based Document Management Access
Access to our Internal Brokerage Forum
Company Profit Sharing!
Private Offices Available to Rent

*Lead Generation Software with over 3,000 Leads
*10 Leads to Start
* Free Personal CRM and Website
*Restrictions and Rules apply

Company Address:
4817 Amberfield Road
Suite 512
Fairfax, VA 22194
Phone: 703-555-0147
email: info@marlowrealty.example

Target Market(s)

Real Estate Agents

Industry/Entity Type

Real Estate

Colors
0555a3
ffffff

Requirements
Must have
• 100% COMMISSION NO MONTHLY FEE
$450 Flat Transaction FEE

What We Offer:
24/7 Office Access
Free Online CE and PLE
Free 1,000 Business Cards
Company Profit Sharing!

*10 Leads to Start

Company Address:
4817 Amberfield Road
Suite 512
Fairfax, VA 22194
Phone: 703-555-0147

```html
<!DOCTYPE html>
<html lang="en">
<head>
<meta charset="utf-8">
<title>Marlow Realty – Agent Recruiting Flyer</title>
<link href="https://fonts.googleapis.com/css2?family=Montserrat:wght@300;500;600;700&display=swap" rel="stylesheet">
<style>
  :root {
    --brand-blue: #0555a3;
    --bright-blue: #0a5cb0;
    --cyan: #0796d6;
    --navy: #0b2a52;
    --ink: #0c0c0c;
    --paper: #f6f7f8;
    --white: #ffffff;
  }
  * { margin: 0; padding: 0; box-sizing: border-box; }
  html, body { width: 852px; height: 1200px; overflow: hidden; background: var(--white); }
  .flyer {
    position: relative;
    width: 852px;
    height: 1200px;
    overflow: hidden;
    background: var(--paper);
    font-family: "Montserrat", sans-serif;
  }
  .backdrop { position: absolute; inset: 0; }

  .headline-rate {
    position: absolute; left: 22px; top: 11px;
    font-size: 138px; font-weight: 700; line-height: 1;
    letter-spacing: -6px; color: var(--bright-blue);
  }
  .headline-commission {
    position: absolute; left: 25px; top: 146px;
    font-size: 44px; font-weight: 600; letter-spacing: -1.2px;
    color: var(--navy); line-height: 1;
  }
  .headline-fee {
    position: absolute; left: 25px; top: 196px;
    font-size: 33px; font-weight: 600; letter-spacing: -1px;
    color: var(--navy); line-height: 1;
  }
  .rule {
    position: absolute; left: 0; height: 2px;
    background: linear-gradient(90deg, var(--brand-blue) 70%, rgba(5,85,163,0));
  }
  .rule-top { top: 247px; width: 325px; }
  .rule-mid { top: 435px; width: 290px; }
  .rule-low { top: 897px; width: 500px; }

  .price {
    position: absolute; left: 22px; top: 264px;
    font-size: 112px; font-weight: 700; letter-spacing: -3px;
    color: var(--ink); line-height: 1;
  }
  .price-label {
    position: absolute; left: 26px; top: 386px;
    font-size: 29px; font-weight: 600; letter-spacing: -0.6px;
    color: var(--ink); line-height: 1;
  }

  .offer-title {
    position: absolute; left: 30px; top: 471px;
    font-size: 21px; font-weight: 600; color: var(--ink);
  }
  .offer-list {
    position: absolute; left: 26px; top: 513px;
    list-style: none;
  }
  .offer-list li {
    font-size: 18px; font-weight: 500; color: var(--bright-blue);
    line-height: 32.5px; white-space: nowrap; letter-spacing: -0.3px;
  }
  .offer-list li::before { content: "•"; margin-right: 8px; font-size: 14px; vertical-align: 2px; }
  .offer-list li.compact { font-size: 15.5px; }

  .lead-notes {
    position: absolute; left: 26px; top: 925px;
    list-style: none;
  }
  .lead-notes li {
    font-size: 19px; font-weight: 500; color: var(--bright-blue);
    line-height: 32.6px; white-space: nowrap; letter-spacing: -0.2px;
  }

  .contact {
    position: absolute; left: 26px; top: 1106px;
    color: var(--white); font-style: normal;
  }
  .contact-line { font-size: 16.5px; font-weight: 600; line-height: 21px; letter-spacing: -0.2px; }
  .contact-license { font-size: 13px; font-weight: 300; margin-top: 10px; }

  .brand-box {
    position: absolute; left: 608px; top: 0; width: 244px; height: 127px;
    background: var(--white); border-bottom-left-radius: 16px;
    display: flex; align-items: center; justify-content: center; gap: 10px;
  }
  .brand-mark { width: 16px; height: 16px; background: var(--brand-blue); }
  .brand-name { font-size: 25px; font-weight: 600; color: var(--brand-blue); letter-spacing: 0.5px; }

  .website {
    position: absolute; left: 778px; top: 698px; height: 462px;
    writing-mode: vertical-rl; transform: rotate(180deg);
    font-size: 33px; font-weight: 700; color: var(--brand-blue);
    letter-spacing: -0.5px; text-align: left; white-space: nowrap;
  }
</style>
</head>
<body>
<main class="flyer">
  <svg class="backdrop" width="852" height="1200" viewBox="0 0 852 1200">
    <defs>
      <linearGradient id="scene-tone" x1="0" y1="0" x2="0.15" y2="1">
        <stop offset="0" stop-color="#2f63b8"/>
        <stop offset="0.18" stop-color="#7d9ad0"/>
        <stop offset="0.4" stop-color="#c9b9a4"/>
        <stop offset="0.6" stop-color="#e4dccd"/>
        <stop offset="0.82" stop-color="#ffffff"/>
      </linearGradient>
    </defs>
    <rect class="footer-band" x="0" y="1090" width="852" height="110" fill="#0b2a52"/>
    <path class="wave-dark" d="M445 0 C390 120 330 230 338 340 C346 470 470 640 530 800 C575 930 600 1060 560 1200 L852 1200 L852 0 Z" fill="#0555a3"/>
    <path class="wave-light" d="M459 0 C404 120 344 230 352 340 C360 470 484 640 544 800 C589 930 628 1060 600 1200 L852 1200 L852 0 Z" fill="#0796d6"/>
    <path class="wave-inner" d="M471 0 C416 120 356 230 364 340 C372 470 496 640 556 800 C601 930 648 1060 640 1200 L852 1200 L852 0 Z" fill="#ffffff"/>
    <path class="scene-photo" role="img" aria-label="Photo of a hand in a dark suit sleeve holding a model house against a blue sky"
      d="M476 0 C421 120 361 230 369 340 C377 470 501 640 561 800 C606 930 656 1060 650 1200 L852 1200 L852 0 Z" fill="url(#scene-tone)"/>
  </svg>

  <div class="brand-box">
    <span class="brand-mark"></span>
    <span class="brand-name">Marlow Realty</span>
  </div>

  <h1 class="headline-rate">100%</h1>
  <p class="headline-commission">COMMISSION</p>
  <p class="headline-fee">NO MONTHLY FEE</p>
  <div class="rule rule-top"></div>

  <p class="price">$450</p>
  <p class="price-label">Flat Transaction FEE</p>
  <div class="rule rule-mid"></div>

  <h2 class="offer-title">What We Offer:</h2>
  <ul class="offer-list">
    <li>24/7 Office Access</li>
    <li>Free E &amp; O Insurance for 1st Year</li>
    <li>Free Online CE and PLE</li>
    <li>Free 1,000 Business Cards</li>
    <li>Free Professional Social Media Marketing</li>
    <li>Free Printing, Scanning, and Copies</li>
    <li>Free Buyer and Seller Presentation Packages</li>
    <li class="compact">Free Filquay Cloud Based Document Management Access</li>
    <li>Access to our Internal Brokerage Forum</li>
    <li>Company Profit Sharing!</li>
    <li>Private Offices Available to Rent</li>
  </ul>
  <div class="rule rule-low"></div>

  <ul class="lead-notes">
    <li>*Lead Generation Software with over 3,000 Leads</li>
    <li>*10 Leads to Start</li>
    <li>* Free Personal CRM and Website</li>
    <li>*Restrictions and Rules apply</li>
  </ul>

  <address class="contact">
    <p class="contact-line">4817 Amberfield Road, Suite 512, Fairfax, VA 22194</p>
    <p class="contact-line">Phone: 703-555-0147 | email: info@marlowrealty.example</p>
    <p class="contact-license">Licensed in D.C., Maryland, and Virginia</p>
  </address>

  <p class="website">www.Marlowrealty.example</p>
</main>
</body>
</html>
```